Create a Graphic About YOURSELF and PixelHarbor

PixelHarbor would like you (designers) to create an awesome graphic to promote YOURSELF and your profile on PixelHarbor!

Your graphic should communicate your name, your services and should mention PixelHarbor.

The design should be perfect for sharing on Chatterly. Here's an example of what we'd like http://blog.pixelharbor-example.ca/article/333/pixelharbor-launches-3000-hire-me-social-design-contest

Once you submitted your design, we'd love you to share the design ('advertisement') and promote yourself and PixelHarbor to your friends and potential customers. So make your submissions great and get your friends to vote for your design by 'Liking' it on Chatterly!

Prizes:
$1500 - "PixelHarbor Community" prize awarded to the designer with the most Chatterly 'Likes'
5 x $50 for the next 5 'most liked' designs on Chatterly

$1000 - "Hire Me" prize awarded to the designer who receives the most client invites
5 x $50 for the next 5 'most invited' designers

In summary, this is a great opportunity for you to increase your exposure to PixelHarbor customers and win cash prizes. Show off your design skills and get hired by PixelHarbor customers from around the world!

Target Market(s)

Fans, friends and customers of YOU

Industry/Entity Type

Cash

Requirements
Must have
• 1) Include your PixelHarbor user name on the graphic so customers can find you in the PixelHarbor Designer Directory
2) Include the tagline "Hire Me on PixelHarbor.com!" in your graphic design.
3) Share your design's URL on our Chatterly wall at http://chatterly-example.com/pixelharbor and get your friends to 'like' your design.
Nice to have
• 1) Include a tagline that expresses your design approach/philosophy
2) Artwork dimensions: 403 x 403 px
3) You can submit more than 1 design!
Should not have
• You must own the copyright of any images you use including stock imagery.

```html
<!DOCTYPE html>
<html lang="en">
<head>
<meta charset="utf-8">
<title>Marisol Ventura — Hire Me on PixelHarbor</title>
<link rel="stylesheet" href="https://fonts.googleapis.com/css2?family=Source+Sans+3:wght@300;400&display=swap">
<style>
  :root {
    --paper: #ffffff;
    --grid: #a9cbe6;
    --moss: #a9b38f;
    --straw: #dedaae;
    --wheat: #c9bf91;
    --sage: #c8d3b5;
    --blush: #ebc9b8;
    --olive-text: #ab9f68;
    --ink-grey: #8a8a8a;
    --ink-dark: #5f6366;
    --brand: #2a6f8f;
  }
  html, body {
    margin: 0;
    padding: 0;
    overflow: hidden;
    background: var(--paper);
  }
  .poster {
    position: relative;
    width: 1200px;
    height: 848px;
    background: var(--paper);
    overflow: hidden;
    font-family: "Source Sans 3", "Helvetica Neue", Arial, sans-serif;
  }
  .block, .photo {
    position: absolute;
    margin: 0;
  }
  .block--moss  { left: 0;    top: 213px; width: 117px; height: 635px; background: var(--moss); }
  .block--straw { left: 117px; top: 108px; width: 121px; height: 316px; background: var(--straw); }
  .block--wheat { left: 238px; top: 213px; width: 123px; height: 211px; background: var(--wheat); }
  .block--sage  { left: 361px; top: 0;    width: 117px; height: 424px; background: var(--sage); }
  .block--blush { left: 478px; top: 213px; width: 123px; height: 211px; background: var(--blush); }
  .block--edge  { left: 1169px; top: 424px; width: 31px; height: 424px; background: var(--blush); }

  .photo--garden { left: 478px; top: 0; width: 123px; height: 213px;
    background: linear-gradient(160deg, #e6e6e2 0%, #b9c6a2 40%, #6f8f4e 100%); }
  .photo--sky { left: 938px; top: 0; width: 126px; height: 105px;
    background: linear-gradient(180deg, #7fa7cf 0%, #b8cbd8 55%, #6d7052 100%); }
  .photo--palm { left: 1064px; top: 105px; width: 105px; height: 108px;
    background: linear-gradient(200deg, #4f6a55 0%, #8fb6dc 45%, #cfe2f2 100%); }
  .photo--web { left: 601px; top: 424px; width: 463px; height: 195px;
    background: linear-gradient(110deg, #6e8a3c 0%, #8f9a5e 35%, #a98c6a 60%, #7f9447 100%); }
  .photo--blossom { left: 361px; top: 619px; width: 240px; height: 229px;
    background: linear-gradient(180deg, #bdd3e6 0%, #9fb4a4 45%, #dfe4dc 70%, #61703f 100%); }

  .grid {
    position: absolute;
    inset: 0;
    pointer-events: none;
  }
  .grid line {
    stroke: var(--grid);
    stroke-width: 1;
    stroke-dasharray: 3 3;
    opacity: 0.85;
  }

  .lead-in {
    position: absolute;
    left: 58px;
    top: 86px;
    margin: 0;
    font-size: 14px;
    color: var(--olive-text);
    line-height: 1;
  }
  .headline {
    position: absolute;
    left: 0;
    top: 0;
    margin: 0;
    font-weight: 300;
    font-size: 108px;
    color: #ffffff;
    line-height: 1;
  }
  .headline span {
    position: absolute;
    top: 288px;
    transform: translateX(-50%);
  }
  .headline .l1 { left: 58px; }
  .headline .l2 { left: 175px; }
  .headline .l3 { left: 287px; }
  .headline .l4 { left: 420px; }
  .headline .l5 { left: 541px; }

  .identity {
    position: absolute;
    left: 716px;
    top: 176px;
    margin: 0;
  }
  .identity__name {
    margin: 0;
    font-size: 25px;
    font-weight: 400;
    color: var(--ink-grey);
    letter-spacing: 0.5px;
    line-height: 1;
  }
  .identity__motto {
    margin: 14px 0 0;
    font-size: 19px;
    color: var(--ink-grey);
    line-height: 1;
  }

  .vertical {
    position: absolute;
    margin: 0;
    writing-mode: vertical-rl;
    transform: rotate(180deg);
    font-size: 15px;
    color: var(--olive-text);
    line-height: 1;
    white-space: nowrap;
  }
  .vertical--creativity { left: 257px; top: 594px; }
  .vertical--is         { left: 335px; top: 620px; }
  .vertical--sense      { left: 465px; top: 418px; }

  .hire {
    position: absolute;
    left: 716px;
    top: 770px;
    margin: 0;
  }
  .hire__call {
    margin: 0 0 0 24px;
    font-size: 29px;
    color: var(--ink-dark);
    line-height: 1;
  }
  .hire__site {
    margin: 2px 0 0;
    display: flex;
    align-items: center;
    gap: 6px;
    font-size: 21px;
    color: var(--brand);
    line-height: 1;
  }
  .hire__dot {
    width: 18px;
    height: 18px;
    border-radius: 50%;
    background: var(--brand);
  }
</style>
</head>
<body>
<main class="poster">
  <div class="block block--moss"></div>
  <div class="block block--straw"></div>
  <div class="block block--wheat"></div>
  <div class="block block--sage"></div>
  <div class="block block--blush"></div>
  <div class="block block--edge"></div>

  <div class="photo photo--garden" role="img" aria-label="Photo of a white garden ornament standing in green grass"></div>
  <div class="photo photo--sky" role="img" aria-label="Photo of blue sky above rooftops and trees"></div>
  <div class="photo photo--palm" role="img" aria-label="Photo of palm fronds against a bright sky"></div>
  <div class="photo photo--web" role="img" aria-label="Close-up photo of a small spider on its web among seed pods"></div>
  <div class="photo photo--blossom" role="img" aria-label="Photo of white blossoms under a soft sky"></div>

  <svg class="grid" width="1200" height="848" viewBox="0 0 1200 848" aria-hidden="true">
    <line x1="51" y1="0" x2="51" y2="848"/>
    <line x1="117" y1="0" x2="117" y2="848"/>
    <line x1="238" y1="0" x2="238" y2="848"/>
    <line x1="281" y1="424" x2="281" y2="848"/>
    <line x1="361" y1="0" x2="361" y2="848"/>
    <line x1="478" y1="0" x2="478" y2="848"/>
    <line x1="601" y1="0" x2="601" y2="848"/>
    <line x1="704" y1="0" x2="704" y2="848"/>
    <line x1="938" y1="0" x2="938" y2="848"/>
    <line x1="1064" y1="0" x2="1064" y2="848"/>
    <line x1="1169" y1="0" x2="1169" y2="848"/>
    <line x1="0" y1="108" x2="1200" y2="108"/>
    <line x1="0" y1="213" x2="1200" y2="213"/>
    <line x1="0" y1="361" x2="601" y2="361"/>
    <line x1="0" y1="424" x2="1200" y2="424"/>
    <line x1="0" y1="619" x2="1200" y2="619"/>
    <line x1="0" y1="731" x2="1200" y2="731"/>
    <line x1="0" y1="826" x2="1200" y2="826"/>
  </svg>

  <p class="lead-in">You can</p>
  <h1 class="headline" aria-label="Build">
    <span class="l1">B</span><span class="l2">U</span><span class="l3">I</span><span class="l4">L</span><span class="l5">D</span>
  </h1>

  <section class="identity">
    <h2 class="identity__name">MARISOL VENTURA</h2>
    <p class="identity__motto">Design change the world</p>
  </section>

  <p class="vertical vertical--creativity">The creativity</p>
  <p class="vertical vertical--is">is</p>
  <p class="vertical vertical--sense">the intelligence of the sense</p>

  <section class="hire">
    <p class="hire__call">HIRE ME ON</p>
    <p class="hire__site"><span class="hire__dot"></span>PixelHarbor.com</p>
  </section>
</main>
</body>
</html>
```